Dog Grooming Coupon Postcard

I need a postcard designed for my dog daycare, boarding and grooming business. This postcard will focus on the Grooming portion of my business. The design should be classy, easy to navigate, inviting and portray experience. We will use this item to mail to dog owners and place on shelves at veterinary clinics and other businesses.

Please find an attached file that can be used as the main graphic.

Information that must be included:
Business Name: The Velvet Kennel
Web Address: www.PlumeRetreats.example
Phone Number: 555-318-4096
Address: 2847 Larkspur Lane Neenah, WI 54956
All of our service areas: Dog Grooming, Overnight Care, Daycare
Logo (I am trying to find our logo file, I will post when I have it. To design around it, go to our website to see what it looks like. It is a square with a paw.)

It would be nice to highlight that we are located in Neenah.

I am open to having a map to show our location.

I want two offers/coupons available: (Please don't make these offers look like a standard coupon, i.e. dashed marks around two square boxes that look like grocery store coupons!)
First: New Client Offer - 20% Off Your Pet's First Grooming Visit
Second:15% Off Any Spa Package

Needs to include this disclaimer: Limit one coupon per household. Not valid with any other offers or coupons. Other restriction or exclusions may apply, call for details.

Our phone number must be large enough to easily read and easily be found.

If there is a way to include some of our grooming services with out taking away from the offers and call to action they include:
Organic Shampoo & Conditioner
Dental Care
Soothing Mud Baths
Flea & Tick Preventative
Shed-Less Treatment
Nail Trim
Haircut
Paw Massage
Spa Packages

I am open to different postcard sizing based on the design.

Target Market(s)

Dog owners who have a disposable income. Age range is 35-65. They are looking for trust and professionalism.

Industry/Entity Type

Grocery Store

Colors

Designer to choose colors to be used in the design.

Requirements
Must have
• Clean, neat design that is easy to read and navigate. Our phone number and a call to action such as, call today for an appointment or schedule an appointment today.

The new client offer should stand out.
Should not have
• Should not have clip art or cartoon looking graphics.

```html
<!DOCTYPE html>
<html lang="en">
<head>
<meta charset="utf-8">
<title>The Velvet Kennel – Grooming Postcard</title>
<link rel="stylesheet" href="https://fonts.googleapis.com/css2?family=Hind:wght@400;500;600;700&display=swap">
<style>
  :root {
    --brown-deep: #5a3c15;
    --brown-mid: #8a6228;
    --gold: #b98a42;
    --gold-light: #c99b52;
    --cream: #ffffff;
    --logo-brown: #5b4a3a;
    --logo-blue: #a9d3dc;
    --photo-dark: #3c3a38;
    --photo-light: #a9a6a2;
  }
  * { margin: 0; padding: 0; box-sizing: border-box; }
  html, body { width: 1200px; height: 797px; overflow: hidden; background: #ffffff; }
  body { font-family: "Hind", "Trebuchet MS", sans-serif; color: var(--cream); }

  .postcard {
    position: relative;
    width: 1200px;
    height: 797px;
    overflow: hidden;
    background: radial-gradient(ellipse 75% 70% at 52% 45%, var(--gold-light) 0%, var(--gold) 40%, var(--brown-mid) 78%, var(--brown-deep) 100%);
  }

  .brand-tab {
    position: absolute;
    left: 26px; top: 0;
    width: 352px; height: 250px;
  }
  .brand-tab svg { position: absolute; inset: 0; }
  .brand-name {
    position: absolute;
    left: 0; right: 0; top: 95px;
    display: flex; flex-direction: column; align-items: center; gap: 14px;
  }
  .brand-mark { width: 60px; height: 60px; background: var(--logo-brown); }
  .brand-text {
    font-size: 36px; font-weight: 500; color: var(--logo-brown);
    letter-spacing: 1px; white-space: nowrap;
  }

  .services-offered {
    position: absolute;
    top: 52px; left: 540px; right: 26px;
    display: flex; justify-content: space-between;
    list-style: none;
    font-size: 31px; font-weight: 600;
  }
  .services-offered li { display: flex; align-items: center; gap: 9px; }
  .services-offered svg { width: 30px; height: 30px; }

  .feature-photo {
    position: absolute;
    left: 490px; top: 198px;
    width: 484px; height: 366px;
    border-radius: 50%;
    border: 5px solid var(--cream);
    background: linear-gradient(110deg, var(--photo-light) 0%, #8e8a86 40%, #6d6a66 65%, var(--photo-dark) 100%);
    overflow: hidden;
  }
  .spa-offer {
    position: absolute;
    left: 560px; top: 296px;
    width: 190px;
    text-align: center;
    font-size: 31px; font-weight: 600; line-height: 1.2;
  }

  .grooming-list {
    position: absolute;
    left: 52px; top: 300px;
    list-style: none;
    font-size: 25px; font-weight: 400; line-height: 39px;
  }
  .grooming-list li { display: flex; align-items: center; gap: 12px; }
  .grooming-list li::before {
    content: ""; width: 14px; height: 14px; border-radius: 50%; background: var(--cream);
  }

  .location, .new-client-offer {
    position: absolute;
    top: 572px;
    text-align: center;
    font-weight: 700; line-height: 40px; font-size: 31px;
  }
  .location { left: 380px; width: 250px; }
  .new-client-offer { left: 690px; width: 480px; }
  .offer-divider {
    position: absolute; left: 663px; top: 578px;
    width: 2px; height: 74px; background: rgba(255,255,255,0.8);
  }

  .disclaimer {
    position: absolute;
    left: 40px; right: 40px; top: 680px;
    text-align: center; font-size: 16.5px;
  }
  .footer-rule {
    position: absolute; left: 54px; right: 54px; top: 714px;
    height: 1px; background: rgba(255,255,255,0.75);
  }
  .contact {
    position: absolute; left: 44px; right: 40px; top: 735px;
    display: flex; align-items: center; justify-content: space-between;
    font-size: 23px;
  }
  .contact span { display: flex; align-items: center; gap: 10px; }
  .contact .phone { font-size: 29px; font-weight: 700; }
  .contact svg { flex: none; }
</style>
</head>
<body>
<main class="postcard">

  <div class="brand-tab">
    <svg width="352" height="250" viewBox="0 0 352 250" aria-hidden="true">
      <path d="M0 0 H352 V225 Q176 262 0 225 Z" fill="#ffffff"/>
    </svg>
    <div class="brand-name">
      <div class="brand-mark"></div>
      <div class="brand-text">The Velvet Kennel</div>
    </div>
  </div>

  <ul class="services-offered">
    <li><svg viewBox="0 0 30 30" aria-hidden="true"><circle cx="15" cy="15" r="12" fill="none" stroke="#fff" stroke-width="2.6"/><path d="M9 15 l5 5 L26 5" fill="none" stroke="#fff" stroke-width="3" stroke-linecap="round" stroke-linejoin="round"/></svg>Dog Grooming</li>
    <li><svg viewBox="0 0 30 30" aria-hidden="true"><circle cx="15" cy="15" r="12" fill="none" stroke="#fff" stroke-width="2.6"/><path d="M9 15 l5 5 L26 5" fill="none" stroke="#fff" stroke-width="3" stroke-linecap="round" stroke-linejoin="round"/></svg>Overnight Care</li>
    <li><svg viewBox="0 0 30 30" aria-hidden="true"><circle cx="15" cy="15" r="12" fill="none" stroke="#fff" stroke-width="2.6"/><path d="M9 15 l5 5 L26 5" fill="none" stroke="#fff" stroke-width="3" stroke-linecap="round" stroke-linejoin="round"/></svg>Day-care</li>
  </ul>

  <div class="feature-photo" role="img" aria-label="Photo of a groomer trimming a dog's paw fur with scissors"></div>
  <p class="spa-offer">15% Off - Any Spa Package</p>

  <ul class="grooming-list">
    <li>Organic Shampoo &amp; Conditioner</li>
    <li>Dental Care</li>
    <li>Soothing Mud Baths</li>
    <li>Flea &amp; Tick Preventative</li>
    <li>Shed-Less Treatment</li>
    <li>Nail Trim</li>
    <li>Haircut</li>
    <li>Paw Massage</li>
    <li>Spa Packages</li>
  </ul>

  <p class="location">we are located in<br>NEENAH</p>
  <div class="offer-divider"></div>
  <p class="new-client-offer">New Client Offer - 20% Off<br>Your Pet's First Grooming Visit</p>

  <p class="disclaimer">Limit one coupon per household. Not valid with any other offers or coupons. Other restriction or exclusions may apply, call for details.</p>
  <div class="footer-rule"></div>

  <div class="contact">
    <span class="phone">
      <svg width="20" height="34" viewBox="0 0 20 34" aria-hidden="true"><rect x="1.5" y="1.5" width="17" height="31" rx="3" fill="none" stroke="#fff" stroke-width="2.4"/><rect x="5" y="6" width="10" height="9" fill="#fff"/><circle cx="10" cy="26" r="2" fill="#fff"/></svg>
      555-318-4096
    </span>
    <span class="address">
      <svg width="18" height="24" viewBox="0 0 18 24" aria-hidden="true"><path d="M9 1 C4.5 1 1 4.5 1 9 C1 15 9 23 9 23 S17 15 17 9 C17 4.5 13.5 1 9 1 Z" fill="#fff"/><circle cx="9" cy="9" r="3" fill="#8a6228"/></svg>
      2847 Larkspur Lane Neenah, WI 54956
    </span>
    <span class="web">
      <svg width="20" height="20" viewBox="0 0 20 20" aria-hidden="true"><circle cx="10" cy="10" r="8.5" fill="none" stroke="#fff" stroke-width="2"/><ellipse cx="10" cy="10" rx="3.5" ry="8.5" fill="none" stroke="#fff" stroke-width="1.6"/><path d="M1.5 10 H18.5" stroke="#fff" stroke-width="1.6"/></svg>
      www.PlumeRetreats.example
    </span>
  </div>

</main>
</body>
</html>
```